Plakat-Design für Saunaanlage nach russischer Art
Zielgruppe
Wir sind eine Saunaanlage nach russischer Art (rus. Banja). Wir bieten Sauna und Erholung in Privatsphäre. Hierzu vermieten wir einzelne Saunahäuser an z.b. Paare zur Alleinnutzung. Zielgruppe 20-70
Aufgabenstellung
Es soll ein Werbeschild an der Strasse werden. 250x250cm
Unser Logo soll drauf.
Öffnungszeiten Mittwoch und Donnerstag 14 bis 22 Uhr. Freitag und Samstag 10 bis 23 Uhr. Sonntag 10 bis 22 Uhr.
Terminvereinbarung unter 02734 5819027 oder 01578924413
Es soll ersichtlich sein, dass es sich um 'Sauna in absoluter Privatsphäre ' handelt.
In russischen Worten русская баня
Bilder von der Anlage
Auffällig z.b. in rot wie ein Stempel 'Zutritt nur für Besucher der Saunaanlage '
www.waldquell-tarvin.de

```html
<!DOCTYPE html>
<html lang="de">
<head>
<meta charset="utf-8">
<title>Waldquell Tarvin – Saunaanlage</title>
<link href="https://fonts.googleapis.com/css2?family=Montserrat:wght@400;500;600;700;800&family=Bitter:ital,wght@1,700&display=swap" rel="stylesheet">
<style>
  :root {
    --brown: #5b3329;
    --green: #6aac3c;
    --ink: #1e1e1e;
    --white: #ffffff;
    --gap: #ffffff;
  }
  * { box-sizing: border-box; margin: 0; padding: 0; }
  html, body { width: 1200px; height: 1200px; overflow: hidden; background: var(--white); }
  .poster {
    position: relative;
    width: 1200px; height: 1200px;
    background: var(--gap);
    font-family: "Montserrat", sans-serif;
  }
  .photo { position: absolute; width: 597px; height: 597px; }
  .photo--sauna-interior { left: 0; top: 0;
    background: linear-gradient(160deg, #c8955a 0%, #e7c18c 40%, #d9b07a 65%, #6b4a2c 100%); }
  .photo--cabin { left: 603px; top: 0;
    background: linear-gradient(180deg, #dfe7ea 0%, #c7d3d8 18%, #8b3e22 30%, #9a4a2a 62%, #3f6b34 80%, #2f5226 100%); }
  .photo--garden { left: 0; top: 603px;
    background: linear-gradient(180deg, #e9eef0 0%, #9a6a42 22%, #8a5a35 55%, #3f8a2e 75%, #2f7424 100%); }
  .photo--lounge { left: 603px; top: 603px;
    background: linear-gradient(135deg, #e5c9a0 0%, #d8b88c 45%, #b35a45 70%, #2a2a2a 100%); }

  .info-card {
    position: absolute; left: 401px; top: 125px;
    width: 407px; height: 732px;
    background: var(--white);
    border-radius: 10px;
    padding: 9px;
  }
  .info-card__frame {
    width: 100%; height: 100%;
    border: 3px solid var(--green);
    border-radius: 8px;
    text-align: center;
    padding-top: 56px;
  }
  .brand { display: flex; align-items: center; justify-content: center; gap: 12px; }
  .brand__mark { width: 26px; height: 26px; background: var(--green); }
  .brand__name { font-weight: 700; font-size: 34px; color: var(--brown); letter-spacing: -0.5px; }
  .brand__tagline { margin-top: 6px; font-size: 12px; font-weight: 500; color: var(--green); }
  .brand__native { margin-top: 4px; font-size: 14px; font-weight: 600; color: var(--brown); }

  .welcome {
    margin-top: 48px;
    font-weight: 800; font-size: 20px; line-height: 1.3;
    color: var(--green); text-transform: uppercase;
  }
  .privacy { margin-top: 6px; font-size: 15px; font-weight: 600; color: var(--brown); }
  .section-title { font-weight: 800; font-size: 20px; color: var(--ink); text-transform: uppercase; }
  .hours { margin-top: 26px; }
  .hours__item { margin-top: 10px; font-size: 17.5px; line-height: 1.35; color: var(--ink); }
  .hours .section-title { margin-bottom: -2px; }
  .booking { margin-top: 26px; }
  .booking__phone { margin-top: 6px; font-size: 17px; color: var(--ink); }
  .website { margin-top: 28px; font-weight: 700; font-size: 19px; color: var(--green); }

  .stamp {
    position: absolute; left: 728px; top: 425px;
    width: 208px; height: 208px; border-radius: 50%;
    background: var(--brown);
    display: flex; flex-direction: column; align-items: center; justify-content: center;
    transform: rotate(-18deg);
    font-family: "Bitter", serif; font-style: italic; font-weight: 700;
    color: var(--white); text-align: center;
  }
  .stamp__lead { font-size: 30px; line-height: 1.1; }
  .stamp__text { font-size: 20px; line-height: 1.15; }
</style>
</head>
<body>
<main class="poster">
  <div class="photo photo--sauna-interior" role="img" aria-label="Saunakabine aus hellem Holz mit Aufgusskübel und Kelle auf der Bank"></div>
  <div class="photo photo--cabin" role="img" aria-label="Rotbraunes Holzsaunahaus mit grüner Tür und Ziegeldach"></div>
  <div class="photo photo--garden" role="img" aria-label="Umzäunter Garten mit Liegestühlen, Kunstrasen und Holzbadefass"></div>
  <div class="photo photo--lounge" role="img" aria-label="Ruheraum mit Ledersofa, Couchtisch, Fernseher und Kamin vor Klinkerwand"></div>

  <section class="info-card">
    <div class="info-card__frame">
      <div class="brand">
        <span class="brand__mark"></span>
        <span class="brand__name">Waldquell Tarvin</span>
      </div>
      <p class="brand__tagline">ein echt russisches Saunaerlebnis</p>
      <p class="brand__native" lang="ru">русская баня</p>

      <h1 class="welcome">Herzlich Willkommen<br>in unserer Saunaanlage!</h1>
      <p class="privacy">Sauna in absoluter Privatsphäre</p>

      <div class="hours">
        <h2 class="section-title">Öffnungszeiten:</h2>
        <p class="hours__item">Mittwoch &amp; Donnerstag<br>14 bis 22 Uhr</p>
        <p class="hours__item">Freitag &amp; Samstag<br>10 bis 23 Uhr</p>
        <p class="hours__item">Sonntag<br>10 bis 22 Uhr</p>
      </div>

      <div class="booking">
        <h2 class="section-title">Terminvereinbarung:</h2>
        <p class="booking__phone">Tel. 02734 5819027 oder 0157 8924413</p>
      </div>

      <p class="website">www.waldquell-tarvin.de</p>
    </div>
  </section>

  <div class="stamp">
    <span class="stamp__lead">Zutritt</span>
    <span class="stamp__text">nur für Besucher<br>der Sauna-<br>anlage.</span>
  </div>
</main>
</body>
</html>
```